Landing Page / Waitlist

I would like a landing page for people to sign up for a waiting list. The text on the page should include (but is not limited to):
1) Main point: The accounting system you'll love
2) Secondary points:
a. Ruthlessly efficient
b. Quietly intelligent
c. Driven by AI
I've attached a file of our logo

The design should be simple, clean, and innovative - this is an ai company

```html
<!DOCTYPE html>
<html lang="en">
<head>
<meta charset="utf-8">
<title>LedgerBloom — Join the Waitlist</title>
<link rel="stylesheet" href="https://fonts.googleapis.com/css2?family=Poppins:wght@400;500;600;700&display=swap">
<style>
  :root {
    --navy-deep: #021a3a;
    --navy: #03306b;
    --blue: #0a5fb8;
    --blue-bright: #1a86e0;
    --white: #ffffff;
    --ink: #1c2233;
    --orange-light: #f7931e;
    --orange: #f26a1b;
    --footer-bg: #02152e;
    --rule: rgba(255,255,255,0.25);
  }
  * { box-sizing: border-box; margin: 0; padding: 0; }
  html, body { width: 1200px; height: 738px; overflow: hidden; }
  body {
    font-family: "Poppins", sans-serif;
    color: var(--white);
    background: var(--navy-deep);
    position: relative;
  }
  .hero-backdrop {
    position: absolute; inset: 0 0 72px 0;
    background:
      radial-gradient(ellipse 60% 55% at 52% 45%, rgba(26,134,224,0.55), transparent 70%),
      radial-gradient(ellipse 40% 60% at 20% 30%, rgba(10,95,184,0.6), transparent 70%),
      linear-gradient(180deg, var(--navy) 0%, #042a5c 55%, var(--navy-deep) 100%);
  }
  .brand-name {
    position: absolute; top: 150px; left: 0; width: 100%;
    text-align: center; font-size: 52px; font-weight: 600;
    letter-spacing: -1px; line-height: 1;
  }
  .headline {
    position: absolute; top: 258px; left: 0; width: 100%;
    text-align: center; font-size: 35px; font-weight: 700; line-height: 1.2;
  }
  .tagline {
    position: absolute; top: 309px; left: 0; width: 100%;
    text-align: center; font-size: 19px; font-weight: 500;
  }
  .feature {
    position: absolute; top: 354px; width: 180px;
    display: flex; flex-direction: column; align-items: center;
  }
  .feature--efficient { left: 318px; }
  .feature--intelligent { left: 512px; }
  .feature--ai { left: 705px; }
  .feature-icon {
    width: 58px; height: 58px; border-radius: 50%;
    border: 1.5px solid var(--white); background: var(--navy-deep);
    display: flex; align-items: center; justify-content: center;
  }
  .feature-label { margin-top: 15px; font-size: 16px; font-weight: 400; letter-spacing: 0.3px; white-space: nowrap; }
  .waitlist-form {
    position: absolute; left: 317px; top: 494px; width: 567px; height: 54px;
    background: var(--white); border-radius: 27px;
  }
  .email-input {
    position: absolute; left: 22px; top: 0; height: 54px; width: 380px;
    border: none; background: transparent; outline: none;
    font-family: "Poppins", sans-serif; font-size: 13px; color: var(--ink);
  }
  .email-input::placeholder { color: var(--ink); }
  .join-button {
    position: absolute; right: 7px; top: 4px; width: 157px; height: 46px;
    border: none; border-radius: 23px; cursor: pointer;
    background: linear-gradient(180deg, var(--orange-light), var(--orange));
    color: var(--white); font-family: "Poppins", sans-serif; font-size: 14px; font-weight: 600;
  }
  .site-footer {
    position: absolute; left: 0; bottom: 0; width: 100%; height: 72px;
    background: var(--footer-bg); border-top: 1px solid var(--rule);
  }
  .copyright {
    position: absolute; top: 30px; width: 100%; text-align: center;
    font-size: 11px; font-weight: 400;
  }
</style>
</head>
<body>
  <div class="hero-backdrop" role="img" aria-label="Blurred blue-toned photo of a person working at a laptop with floating document and AI chip graphics"></div>

  <div class="brand-name">LedgerBloom</div>

  <h1 class="headline">Welcome to LedgerBloom</h1>
  <p class="tagline">The accounting system you'll love</p>

  <div class="feature feature--efficient">
    <div class="feature-icon">
      <svg width="30" height="30" viewBox="0 0 30 30" fill="none" stroke="#fff" stroke-width="1.4">
        <path d="M3 27h24"/><rect x="5" y="17" width="4" height="10"/><rect x="12" y="13" width="4" height="14"/><rect x="19" y="9" width="4" height="18"/>
        <path d="M4 14l7-5 5 3 9-8"/><path d="M21 4h4v4"/>
      </svg>
    </div>
    <div class="feature-label">Ruthlessly Efficient</div>
  </div>

  <div class="feature feature--intelligent">
    <div class="feature-icon">
      <svg width="30" height="30" viewBox="0 0 30 30" fill="none" stroke="#fff" stroke-width="1.4">
        <rect x="4" y="5" width="22" height="15" rx="1.5"/><path d="M11 25h8M15 20v5"/>
        <path d="M8 10h8M8 13h12M8 16h6"/><circle cx="21" cy="10" r="1.5"/>
      </svg>
    </div>
    <div class="feature-label">Quietly Intelligent</div>
  </div>

  <div class="feature feature--ai">
    <div class="feature-icon">
      <svg width="30" height="30" viewBox="0 0 30 30" fill="none" stroke="#fff" stroke-width="1.4">
        <rect x="8" y="8" width="14" height="14" rx="1"/>
        <path d="M11 3v5M15 3v5M19 3v5M11 22v5M15 22v5M19 22v5M3 11h5M3 15h5M3 19h5M22 11h5M22 15h5M22 19h5"/>
        <text x="15" y="18" text-anchor="middle" font-family="Poppins, sans-serif" font-size="7" fill="#fff" stroke="none">AI</text>
      </svg>
    </div>
    <div class="feature-label">Driven by AI</div>
  </div>

  <form class="waitlist-form">
    <input class="email-input" type="email" placeholder="Enter Email Address" aria-label="Email address">
    <button class="join-button" type="button">Join the Waitlist</button>
  </form>

  <footer class="site-footer">
    <p class="copyright">Copyright 2025 © CompanyName&nbsp; All Right Reserved</p>
  </footer>
</body>
</html>
```